Corvena Business Card Design

We are the largest used car company fro JapanJust need a simple business cards to start with

Industry/Entity Type

Used Car

Contact Information for Business Card

Mitsuko " Ned" Fujisawa
Operations Director
Corvena Australia Pty.Ltd.
P.O.Box 517 Pennfield NSW 2091
M: 0491 570 156
P: 1800 160 401
email : mitsuko.fujisawa@crv-example.co.jp

```html
<!DOCTYPE html>
<html lang="en">
<head>
<meta charset="utf-8">
<title>Corvena Australia – Business Card</title>
<link rel="stylesheet" href="https://fonts.googleapis.com/css2?family=PT+Sans:wght@400;700&display=swap">
<style>
  :root {
    --teal: #1fb2c8;
    --ink: #263238;
    --ink-soft: #4a5257;
    --paper: #f4f4f4;
    --pattern-a: #ededed;
    --pattern-b: #dedede;
    --green: #00f080;
    --blue: #1ab3cf;
    --pink: #ff2f98;
    --orange: #ff5200;
    --band-gap: #121212;
    --base-light: #e4e4e4;
    --base-dark: #b3b3b3;
    --white: #ffffff;
  }
  * { margin: 0; padding: 0; box-sizing: border-box; }
  html, body {
    width: 1200px; height: 720px; overflow: hidden;
    background: var(--paper);
  }
  .card {
    position: relative; width: 1200px; height: 720px; overflow: hidden;
    font-family: "PT Sans", "Myriad Pro", Arial, sans-serif;
  }
  .floral-backdrop {
    position: absolute; inset: 0;
    background: radial-gradient(ellipse at 30% 25%, var(--pattern-a) 0%, var(--pattern-b) 100%);
  }
  .stripes { position: absolute; inset: 0; }
  .identity { position: absolute; left: 80px; top: 0; color: var(--ink); }
  .company {
    position: absolute; top: 290px; white-space: nowrap;
    font-size: 38px; line-height: 1; letter-spacing: 0.2px;
  }
  .company .brand { color: var(--teal); }
  .address {
    position: absolute; top: 333px; white-space: nowrap;
    font-size: 20px; color: var(--ink-soft);
  }
  .divider {
    position: absolute; top: 377px; left: 0; width: 590px; height: 2px;
    background: var(--ink-soft);
  }
  .person {
    position: absolute; top: 396px; white-space: nowrap;
    font-size: 41px; line-height: 1;
  }
  .person .nickname { color: var(--teal); }
  .role {
    position: absolute; top: 440px; white-space: nowrap;
    font-size: 22px; color: var(--ink-soft);
  }
  .band-text {
    font-family: "PT Sans", "Myriad Pro", Arial, sans-serif;
    font-size: 23px; fill: var(--white);
  }
</style>
</head>
<body>
<div class="card">
  <div class="floral-backdrop" role="img" aria-label="Soft grey floral damask pattern background"></div>

  <svg class="stripes" width="1200" height="720" viewBox="0 0 1200 720" aria-hidden="true">
    <!-- base below bands -->
    <polygon points="0,925 974,520 1200,674 1200,720 0,720" fill="var(--base-light)"/>
    <polygon points="974,520 1200,674 1200,720 974,720" fill="var(--base-dark)"/>

    <!-- pale rising stripes on the right -->
    <polygon points="974,267 1200,173 1200,222 974,315" fill="#c6f7e0" opacity="0.85"/>
    <polygon points="974,325 1200,231 1200,290 974,384" fill="#c4e9f2" opacity="0.85"/>
    <polygon points="974,391 1200,297 1200,354 974,448" fill="#ffd3e6" opacity="0.85"/>
    <polygon points="974,455 1200,361 1200,413 974,507" fill="#ffdcc9" opacity="0.85"/>

    <!-- dark separator body -->
    <polygon points="0,672 974,267 1200,421 1200,674 974,520 0,925" fill="var(--band-gap)"/>

    <!-- coloured bands -->
    <polygon points="0,672 974,267 1200,421 1200,469 974,315 0,720" fill="var(--green)"/>
    <polygon points="0,730 974,325 1200,479 1200,538 974,384 0,789" fill="var(--blue)"/>
    <polygon points="0,796 974,391 1200,545 1200,602 974,448 0,853" fill="var(--pink)"/>
    <polygon points="0,860 974,455 1200,609 1200,661 974,507 0,912" fill="var(--orange)"/>

    <!-- shading on descending face -->
    <polygon points="974,267 1200,421 1200,674 974,520" fill="#000" opacity="0.18"/>

    <!-- contact text on bands -->
    <g transform="translate(960 360) rotate(-22.58)">
      <text class="band-text" x="0" y="8" text-anchor="end">M: 0491 570 156  P: 1800 160 401</text>
    </g>
    <g transform="translate(960 425) rotate(-22.58)">
      <text class="band-text" x="0" y="8" text-anchor="end">corvenaaustralia@example.com</text>
    </g>
    <g transform="translate(960 487) rotate(-22.58)">
      <text class="band-text" x="0" y="8" text-anchor="end">corvenaus.com</text>
    </g>

    <!-- icons -->
    <g class="icon-phone" fill="var(--white)" transform="translate(989,331)">
      <path d="M2,6 Q11,0 20,6 L18,10 L14,9 L13,6 Q11,5 9,6 L8,9 L4,10 Z"/>
      <rect x="5" y="10" width="12" height="8" rx="1"/>
    </g>
    <g class="icon-mail" transform="translate(989,397)">
      <rect x="1" y="1" width="20" height="14" fill="var(--white)"/>
      <polyline points="1,1 11,9 21,1" fill="none" stroke="#9a9a9a" stroke-width="1.5"/>
    </g>
    <g class="icon-link" fill="none" stroke="var(--white)" stroke-width="3" transform="translate(990,459) rotate(-45 10 9)">
      <rect x="0" y="4" width="11" height="9" rx="4.5"/>
      <rect x="9" y="4" width="11" height="9" rx="4.5"/>
    </g>
  </svg>

  <div class="identity">
    <div class="company"><span class="brand">CORVENA AUSTRALIA</span> PTY.LTD.</div>
    <div class="address">P.O.Box 517 Pennfield NSW 2091</div>
    <div class="divider"></div>
    <div class="person">MITSUKO <span class="nickname">" NED"</span> FUJISAWA</div>
    <div class="role">Operations Director</div>
  </div>
</div>
</body>
</html>
```